New Creative Busines Card

Hi Lead Designer,

How are you going?

I was hoping you can help me design the perfect business card for my new business. I have listed below some background information about the business and the concept to help with your design. I'm open to any form of creative ideas, but would like to have two types of colour schemes one dark color and one light.

I would like to have a dark set of design and a light (One design with one in black or dark background and one with light background to compare the contrast since the business card will be double sided one) I imagine this will be pretty easy to change the background of the design. Would prefer one side to have all the details and the other will just have a amazing logo (K7) to give it the finishing touch.

Feel free to email me if you have any questions.

Business Structure and design concepts:

Name of the business: K7 Advisory
Business: Dating agency and event management (Date night etc)
Concept: The main focus will be the K7 ( As some sort of a heart shape like logo) be creative
Details to include in the card will be general details like Name, Title: , Email, mobile, website (Contact details will be given later).

The rest of the idea is up to you, feel free to go crazy with your creative ideas.

Thank you for your help in advance, may the best candidate win~!

Target Market(s)

Target market will be Professional, Elegant, young and ambitious people.

Industry/Entity Type

Business

Requirements
Must have
• Focus on the K7 (as some sort of a heart shape logo). Since this is a double sides design would prefer on one side to focus on the just the K7 logo and the other side with a smaller version of the logo (with it or without) and all the details such as Name, Title, Mobile, Email, Website. Please have the design in landscape format.Not fuss with the Font as long as it is easy to read.
Nice to have
• Different Contrast in colours (keep it simple) one side dark colour scheme and one side light. Prefer to have 3-4 colours (not overwhelm with too many colours) to keep it simple and elegant.
Should not have
• Too colours, main focus is should be the K7 logo not the colours

```html
<!DOCTYPE html>
<html lang="en">
<head>
<meta charset="utf-8">
<title>K7 Advisory – Business Card Concepts</title>
<link href="https://fonts.googleapis.com/css2?family=Lustria&family=Great+Vibes&display=swap" rel="stylesheet">
<style>
  :root {
    --berry: #8e2260;
    --berry-deep: #7e1b54;
    --silver-light: #f7f7f7;
    --silver-mid: #e2e2e2;
    --silver-dark: #c9c9c9;
    --ink: #333333;
    --white: #ffffff;
    --page: #ffffff;
  }
  * { margin: 0; padding: 0; box-sizing: border-box; }
  html, body { width: 1200px; height: 801px; overflow: hidden; background: var(--page); }
  .board { position: relative; width: 1200px; height: 801px; font-family: "Lustria", Georgia, serif; }

  .option-label { position: absolute; font-family: Arial, Helvetica, sans-serif; font-size: 26px; color: #222; }
  .option-label--one { left: 305px; top: 27px; }
  .option-label--two { left: 888px; top: 32px; }

  .card { position: absolute; width: 537px; height: 323px; border-radius: 40px; overflow: hidden;
          box-shadow: 0 4px 12px rgba(0,0,0,0.18); }
  .card--dark { background: var(--berry); }
  .card--silver { background: linear-gradient(135deg, var(--silver-light) 0%, var(--silver-mid) 55%, var(--silver-dark) 100%); }
  .card--split { background: linear-gradient(120deg, var(--silver-dark) 0%, var(--silver-light) 40%, var(--silver-mid) 70%, var(--silver-light) 100%); }

  .front-one { left: 38px; top: 77px; }
  .front-two { left: 633px; top: 80px; }
  .back-one  { left: 45px; top: 453px; }
  .back-two  { left: 640px; top: 452px; }

  .card-shape { position: absolute; inset: 0; width: 100%; height: 100%; }

  .mark { position: absolute; width: 100%; text-align: center; line-height: 1; font-size: 120px; }
  .mark--white { color: var(--white); }
  .mark--berry { color: var(--berry); }
  .mark--small { width: auto; font-size: 78px; }

  .brand-name { position: absolute; width: 100%; text-align: center; line-height: 1; font-size: 27px; }
  .brand-name--white { color: var(--white); }
  .brand-name--berry { color: var(--berry); font-size: 23px; }
  .brand-name--small { width: auto; font-size: 15px; color: var(--berry); }

  .tagline { position: absolute; width: 100%; text-align: center; line-height: 1;
             font-family: "Great Vibes", cursive; font-size: 37px; }
  .tagline--white { color: var(--white); }
  .tagline--berry { color: var(--berry); font-size: 39px; }

  .contact { position: absolute; color: var(--ink); }
  .contact-name { font-size: 19px; margin-bottom: 12px; line-height: 1; }
  .contact-list { list-style: none; }
  .contact-item { display: flex; align-items: center; font-size: 17px; line-height: 1; height: 30px; }
  .contact-icon { width: 14px; height: 14px; margin-right: 13px; flex: none; }
  .back-two .contact-name { font-size: 18px; margin-bottom: 10px; }
  .back-two .contact-item { font-size: 16px; height: 28.5px; }
</style>
</head>
<body>
<div class="board">
  <div class="option-label option-label--one">1</div>
  <div class="option-label option-label--two">2</div>

  <!-- Concept 1 – dark front -->
  <section class="card card--dark front-one">
    <div class="mark mark--white" style="top:55px;">K7</div>
    <div class="brand-name brand-name--white" style="top:202px;">K7 Advisory</div>
    <div class="tagline tagline--white" style="top:252px;">Dating Agency &amp; Event Management</div>
  </section>

  <!-- Concept 2 – split front -->
  <section class="card card--split front-two">
    <svg class="card-shape" viewBox="0 0 537 323" preserveAspectRatio="none" aria-hidden="true">
      <path d="M0 0 H537 V200 C440 198 340 208 268 222 C190 210 90 212 0 226 Z" fill="var(--berry)"/>
    </svg>
    <div class="mark mark--white" style="top:45px;">K7</div>
    <div class="brand-name brand-name--berry" style="top:229px;">K7 Advisory</div>
    <div class="tagline tagline--berry" style="top:262px;">Dating Agency &amp; Event Management</div>
  </section>

  <!-- Concept 1 – silver back -->
  <section class="card card--silver back-one">
    <div class="mark mark--berry mark--small" style="left:72px; top:88px;">K7</div>
    <div class="brand-name brand-name--small" style="left:66px; top:180px;">K7 Advisory</div>
    <div class="contact" style="left:225px; top:88px;">
      <p class="contact-name">Name Surname</p>
      <ul class="contact-list">
        <li class="contact-item">
          <svg class="contact-icon" viewBox="0 0 16 16" aria-hidden="true"><path d="M3 1 L6 1 L7 5 L5 6.5 C6 9 7 10 9.5 11 L11 9 L15 10 L15 13 C15 14 14 15 13 15 C6 15 1 10 1 3 C1 2 2 1 3 1 Z" fill="var(--berry)"/></svg>
          123-456-7890
        </li>
        <li class="contact-item">
          <svg class="contact-icon" viewBox="0 0 16 16" aria-hidden="true"><rect x="3.5" y="1" width="9" height="14" rx="1.5" fill="none" stroke="var(--berry)" stroke-width="1.6"/><circle cx="8" cy="12.5" r="0.9" fill="var(--berry)"/></svg>
          123-456-7888
        </li>
        <li class="contact-item">
          <svg class="contact-icon" viewBox="0 0 16 16" aria-hidden="true"><rect x="1" y="3" width="14" height="10" fill="none" stroke="var(--berry)" stroke-width="1.6"/><path d="M1 3 L8 9 L15 3" fill="none" stroke="var(--berry)" stroke-width="1.6"/></svg>
          name@mailbox.com
        </li>
        <li class="contact-item">
          <svg class="contact-icon" viewBox="0 0 16 16" aria-hidden="true"><circle cx="8" cy="8" r="6.5" fill="none" stroke="var(--berry)" stroke-width="1.5"/><ellipse cx="8" cy="8" rx="3" ry="6.5" fill="none" stroke="var(--berry)" stroke-width="1.2"/><path d="M1.5 8 H14.5 M2.5 4.8 H13.5 M2.5 11.2 H13.5" stroke="var(--berry)" stroke-width="1.1"/></svg>
          www.name.com
        </li>
      </ul>
    </div>
  </section>

  <!-- Concept 2 – split back -->
  <section class="card card--split back-two">
    <svg class="card-shape" viewBox="0 0 537 325" preserveAspectRatio="none" aria-hidden="true">
      <path d="M0 0 H537 V72 C390 72 300 90 266 132 C236 92 160 78 0 78 Z" fill="var(--berry)"/>
    </svg>
    <div class="tagline tagline--white" style="top:27px;">Dating Agency &amp; Event Management</div>
    <div class="mark mark--berry mark--small" style="left:62px; top:153px; font-size:90px;">K7</div>
    <div class="contact" style="left:266px; top:148px;">
      <p class="contact-name">Name Surname</p>
      <ul class="contact-list">
        <li class="contact-item">
          <svg class="contact-icon" viewBox="0 0 16 16" aria-hidden="true"><path d="M3 1 L6 1 L7 5 L5 6.5 C6 9 7 10 9.5 11 L11 9 L15 10 L15 13 C15 14 14 15 13 15 C6 15 1 10 1 3 C1 2 2 1 3 1 Z" fill="var(--berry)"/></svg>
          123-456-7890
        </li>
        <li class="contact-item">
          <svg class="contact-icon" viewBox="0 0 16 16" aria-hidden="true"><rect x="3.5" y="1" width="9" height="14" rx="1.5" fill="none" stroke="var(--berry)" stroke-width="1.6"/><circle cx="8" cy="12.5" r="0.9" fill="var(--berry)"/></svg>
          123-456-7888
        </li>
        <li class="contact-item">
          <svg class="contact-icon" viewBox="0 0 16 16" aria-hidden="true"><rect x="1" y="3" width="14" height="10" fill="none" stroke="var(--berry)" stroke-width="1.6"/><path d="M1 3 L8 9 L15 3" fill="none" stroke="var(--berry)" stroke-width="1.6"/></svg>
          name@mailbox.com
        </li>
        <li class="contact-item">
          <svg class="contact-icon" viewBox="0 0 16 16" aria-hidden="true"><circle cx="8" cy="8" r="6.5" fill="none" stroke="var(--berry)" stroke-width="1.5"/><ellipse cx="8" cy="8" rx="3" ry="6.5" fill="none" stroke="var(--berry)" stroke-width="1.2"/><path d="M1.5 8 H14.5 M2.5 4.8 H13.5 M2.5 11.2 H13.5" stroke="var(--berry)" stroke-width="1.1"/></svg>
          www.name.com
        </li>
      </ul>
    </div>
  </section>
</div>
</body>
</html>
```